Business Consultancy Business Card Design

Business Card design required for Business Analysis and Project Consultancy business based in Scotland.

Company Name - Brevick Advisory

Back - Company Logo

Front Details

Owen Brevick
07642 918 305
owen.brevick@brevickadvisory.com
http://www.brevickadvisory.com

Colours should match the logo colours but I am open to design ideas.

```html
<!DOCTYPE html>
<html lang="en">
<head>
<meta charset="utf-8">
<title>Brevick Advisory – Business Cards</title>
<link rel="stylesheet" href="https://fonts.googleapis.com/css2?family=Ubuntu:wght@400;500&display=swap">
<style>
  :root {
    --brand-blue: #009ddc;
    --brand-green: #6db33f;
    --card-dark: #3a393b;
    --text-white: #ffffff;
    --text-grey: #8c8c8e;
    --text-light: #c9c9cb;
    --page-bg: #ffffff;
  }
  * { margin: 0; padding: 0; box-sizing: border-box; }
  html, body {
    width: 1200px; height: 1000px; overflow: hidden;
    background: var(--page-bg);
    font-family: "Ubuntu", sans-serif;
  }
  .canvas { position: relative; width: 1200px; height: 1000px; }

  .card {
    position: absolute;
    width: 638px; height: 412px;
    overflow: hidden;
    box-shadow: 0 6px 14px rgba(0,0,0,0.35);
  }
  .card--logo { left: 258px; top: 62px; background: var(--brand-blue); }
  .card--details { left: 256px; top: 530px; background: var(--card-dark); }

  .wordmark {
    position: absolute;
    display: flex; align-items: center; gap: 14px;
    text-transform: uppercase; white-space: nowrap;
    font-weight: 400;
  }
  .wordmark__dot { border-radius: 50%; flex: none; }
  .card--logo .wordmark { left: 64px; top: 186px; color: var(--text-white); font-size: 33px; }
  .card--logo .wordmark__dot { width: 36px; height: 36px; background: var(--text-white); }
  .card--details .wordmark { left: 68px; top: 58px; color: var(--text-grey); font-size: 25px; }
  .card--details .wordmark__dot { width: 26px; height: 26px; background: var(--brand-blue); }

  .card__accent-circle {
    position: absolute;
    left: 462px; top: 20px;
    width: 370px; height: 370px; border-radius: 50%;
    background: var(--brand-blue);
  }

  .contact { position: absolute; left: 139px; top: 170px; }
  .contact__name { color: var(--text-white); font-size: 27px; font-weight: 400; line-height: 1.2; }
  .contact__phone { color: var(--brand-blue); font-size: 20px; font-weight: 500; margin-top: 8px; letter-spacing: 0.5px; }
  .contact__email { color: var(--text-light); font-size: 15px; margin-top: 1px; }

  .card__green-bar {
    position: absolute; left: 0; top: 343px;
    width: 128px; height: 50px; background: var(--brand-green);
  }
  .website {
    position: absolute; left: 139px; top: 354px;
    color: var(--brand-blue); font-size: 20px; letter-spacing: 5.2px;
  }
</style>
</head>
<body>
<main class="canvas">
  <section class="card card--logo" aria-label="Card back">
    <div class="wordmark"><span class="wordmark__dot"></span>Brevick Advisory</div>
  </section>

  <section class="card card--details" aria-label="Card front">
    <div class="card__accent-circle"></div>
    <div class="wordmark"><span class="wordmark__dot"></span>Brevick Advisory</div>
    <div class="contact">
      <p class="contact__name">Owen Brevick</p>
      <p class="contact__phone">07642 918 305</p>
      <p class="contact__email">owen.brevick@brevickadvisory.com</p>
    </div>
    <div class="card__green-bar"></div>
    <p class="website">www.brevickadvisory.com</p>
  </section>
</main>
</body>
</html>
```